Online-Marketing-Material für Steuerberater und Unternehmensberater
Zielgruppe
Ich bin Steuerberater und Unternehmensberater, Business-Coach.
Meine Zielgruppe sind KMU, deren Mitarbeitern und die Geschäftsführung
Aufgabenstellung
Ich benötige ein Banner für Zunftlo, Filmaro und Plauderhof
folgende Stichworte sollen vorkommen:
- Steuerberatung
- Unternehmensberatung
- Organisationsentwicklung
- agile Arbeitsmethoden
- Employer Branding
- Business-Coaching
- Change Management

```html
<!DOCTYPE html>
<html lang="de">
<head>
<meta charset="utf-8">
<title>Banner Steuer- und Unternehmensberatung</title>
<link rel="stylesheet" href="https://fonts.googleapis.com/css2?family=Montserrat:wght@300;700&family=Poppins:wght@400;500;600&display=swap">
<style>
  :root {
    --page-bg: #ecedf0;
    --navy: #3d5a99;
    --navy-deep: #31497f;
    --accent-green: #8cc63f;
    --tick-blue: #1f56b3;
    --ink: #1c1c1c;
    --mist-top: #f3f4f6;
    --mist-bottom: #d9dce1;
    --white: #ffffff;
  }
  * { margin: 0; padding: 0; box-sizing: border-box; }
  html, body { width: 1200px; height: 960px; overflow: hidden; }
  body {
    background: var(--page-bg);
    font-family: "Poppins", sans-serif;
    display: flex;
    align-items: center;
    justify-content: center;
  }
  .banner {
    position: relative;
    width: 1200px;
    height: 302px;
    overflow: hidden;
    background: var(--white);
  }
  .skyline-backdrop {
    position: absolute;
    inset: 0;
    background: linear-gradient(180deg, var(--mist-top) 0%, #e8eaee 45%, var(--mist-bottom) 100%);
  }
  .navy-field {
    position: absolute;
    inset: 0;
    width: 100%;
    height: 100%;
  }
  .line-illustration {
    position: absolute;
    left: 0;
    top: 0;
    width: 262px;
    height: 302px;
    background: linear-gradient(160deg, #4a67a5 0%, var(--navy) 60%, var(--navy-deep) 100%);
  }
  .headline {
    position: absolute;
    left: 293px;
    top: 34px;
    font-family: "Montserrat", sans-serif;
    color: var(--white);
    font-weight: 300;
    font-size: 47px;
    line-height: 60px;
    letter-spacing: -0.5px;
  }
  .headline .highlight {
    display: block;
    color: var(--accent-green);
    font-weight: 700;
    letter-spacing: -1px;
  }
  .contact {
    position: absolute;
    left: 297px;
    top: 241px;
    color: var(--white);
    font-size: 15.5px;
    line-height: 20px;
    font-weight: 400;
  }
  .contact strong { font-weight: 600; }
  .service-list {
    position: absolute;
    top: 48px;
    list-style: none;
  }
  .service-list--primary { left: 686px; }
  .service-list--secondary { left: 957px; }
  .service-list li {
    display: flex;
    align-items: center;
    height: 36.6px;
    font-size: 16.5px;
    color: var(--ink);
    font-weight: 500;
  }
  .service-list svg { width: 32px; height: 26px; margin-right: 5px; flex: none; }
  .firm-name {
    position: absolute;
    top: 240px;
    display: flex;
    align-items: center;
    gap: 8px;
    font-family: "Poppins", sans-serif;
    font-weight: 600;
    font-size: 20px;
    color: var(--tick-blue);
    letter-spacing: 0.5px;
  }
  .firm-name--tax { left: 722px; }
  .firm-name--consulting { left: 990px; }
  .firm-name .marker {
    width: 14px;
    height: 14px;
    background: var(--tick-blue);
  }
</style>
</head>
<body>
  <section class="banner">
    <div class="skyline-backdrop" role="img" aria-label="Verblasste Stadtsilhouette mit Hochhäusern im Dunst"></div>

    <svg class="navy-field" viewBox="0 0 1200 302" preserveAspectRatio="none" aria-hidden="true">
      <path d="M0 0 H615 C655 60 662 200 625 302 H0 Z" fill="var(--navy)"/>
    </svg>

    <div class="line-illustration" role="img" aria-label="Weiße Strichillustration: Dokument mit Dollarzeichen, Personensymbol und Sprechblase"></div>

    <h1 class="headline">
      Verbessern<br>
      Sie mit uns
      <span class="highlight">Ihr Geschäft!</span>
    </h1>

    <p class="contact">
      Am Lindenhang 17, 50999 Musterstadt<br>
      <strong>Tel:</strong> +49 2200 1234567
    </p>

    <ul class="service-list service-list--primary">
      <li><svg viewBox="0 0 32 26"><path d="M2 14 L11 23 L30 2" fill="none" stroke="var(--tick-blue)" stroke-width="4" stroke-linecap="round" stroke-linejoin="round"/></svg>Steuerberatung</li>
      <li><svg viewBox="0 0 32 26"><path d="M2 14 L11 23 L30 2" fill="none" stroke="var(--tick-blue)" stroke-width="4" stroke-linecap="round" stroke-linejoin="round"/></svg>Unternehmensberatung</li>
      <li><svg viewBox="0 0 32 26"><path d="M2 14 L11 23 L30 2" fill="none" stroke="var(--tick-blue)" stroke-width="4" stroke-linecap="round" stroke-linejoin="round"/></svg>Organisationsentwicklung</li>
      <li><svg viewBox="0 0 32 26"><path d="M2 14 L11 23 L30 2" fill="none" stroke="var(--tick-blue)" stroke-width="4" stroke-linecap="round" stroke-linejoin="round"/></svg>agile Arbeitsmethoden</li>
    </ul>

    <ul class="service-list service-list--secondary">
      <li><svg viewBox="0 0 32 26"><path d="M2 14 L11 23 L30 2" fill="none" stroke="var(--tick-blue)" stroke-width="4" stroke-linecap="round" stroke-linejoin="round"/></svg>Employer Branding</li>
      <li><svg viewBox="0 0 32 26"><path d="M2 14 L11 23 L30 2" fill="none" stroke="var(--tick-blue)" stroke-width="4" stroke-linecap="round" stroke-linejoin="round"/></svg>Business-Coaching</li>
      <li><svg viewBox="0 0 32 26"><path d="M2 14 L11 23 L30 2" fill="none" stroke="var(--tick-blue)" stroke-width="4" stroke-linecap="round" stroke-linejoin="round"/></svg>Change Management</li>
    </ul>

    <div class="firm-name firm-name--tax"><span class="marker"></span>Jonas Brenner</div>
    <div class="firm-name firm-name--consulting"><span class="marker"></span>Veloria GmbH</div>
  </section>
</body>
</html>
```